International Luxury Furniture and Accessories Outsourcing Company

We Need a Business Card design for a new Outsourcing company doing Business Internationally in the Luxury Furniture and Accessories Space. The company's name is CORVIN HALDEN and we deal with clients in the high end and Luxury Space for Furniture and Accessories in the world. We would like Designs that speaks Luxury and Professionalism.

We like the Combination of the color Brown and Gold or Black and Gold. We are also open to other color combo.

We like some of the design of file attached.
Updates

This is Marcus and We really appreciate all of you taking the time out and putting the effort to help us jump start our new company. We have 2-3 designs that we like and will decide soon to pick one. Once again, Thank you to all of you !! Best Regards, Marcus

Industry/Entity Type

Business

```html
<!DOCTYPE html>
<html lang="en">
<head>
<meta charset="utf-8">
<title>Corvin Halden — Business Card</title>
<link rel="stylesheet" href="https://fonts.googleapis.com/css2?family=Open+Sans:wght@300;400;700&display=swap">
<style>
  :root {
    --page: #e9e4dc;
    --card: #2a1d16;
    --card-deep: #231812;
    --gold: #c9a43c;
    --gold-light: #e3c766;
    --ink: #f3ede3;
  }
  * { margin: 0; padding: 0; box-sizing: border-box; }
  html, body {
    width: 1200px;
    height: 784px;
    overflow: hidden;
    background: var(--page);
    font-family: "Open Sans", Arial, sans-serif;
  }
  .sheet {
    position: relative;
    width: 1200px;
    height: 784px;
    display: flex;
    align-items: center;
    justify-content: center;
    gap: 40px;
  }
  .card {
    position: relative;
    width: 540px;
    height: 310px;
    background: var(--card);
    box-shadow: 0 10px 28px rgba(0, 0, 0, 0.22);
    overflow: hidden;
  }

  /* Back side */
  .person {
    position: absolute;
    left: 34px;
    top: 36px;
  }
  .person-name {
    color: var(--gold);
    font-weight: 700;
    font-size: 19px;
    line-height: 1.1;
  }
  .person-title {
    color: var(--ink);
    font-size: 11.5px;
    margin-top: 4px;
  }
  .contact-list {
    position: absolute;
    left: 34px;
    top: 150px;
    list-style: none;
  }
  .contact-list li {
    display: flex;
    align-items: flex-start;
    color: var(--ink);
    font-size: 13px;
    line-height: 17px;
  }
  .contact-list .icon {
    width: 13px;
    height: 13px;
    margin: 2px 10px 0 0;
    flex: none;
    fill: var(--gold);
  }

  /* Front side */
  .card-front { background: var(--card-deep); }
  .frame-outer {
    position: absolute;
    inset: 16px;
    border: 5px solid var(--gold);
  }
  .frame-inner {
    position: absolute;
    inset: 26px;
    border: 1.5px solid var(--gold-light);
  }
  .brand {
    position: absolute;
    left: 0;
    right: 0;
    top: 88px;
    display: flex;
    flex-direction: column;
    align-items: center;
  }
  .brand-square {
    width: 70px;
    height: 70px;
    background: var(--gold);
  }
  .brand-name {
    margin-top: 14px;
    color: var(--gold);
    font-weight: 300;
    font-size: 26px;
    letter-spacing: 2px;
    text-transform: uppercase;
  }
</style>
</head>
<body>
<main class="sheet">

  <section class="card card-back" aria-label="Card back">
    <div class="person">
      <p class="person-name">Corvin Halden</p>
      <p class="person-title">Founder / Managing Director</p>
    </div>

    <ul class="contact-list">
      <li>
        <svg class="icon" viewBox="0 0 12 12"><path d="M6 0a4 4 0 0 0-4 4c0 3 4 8 4 8s4-5 4-8a4 4 0 0 0-4-4zm0 5.5A1.5 1.5 0 1 1 6 2.5a1.5 1.5 0 0 1 0 3z"/></svg>
        <span>2480 Larkmoor Avenue<br>Fairhaven, CA 90000</span>
      </li>
      <li>
        <svg class="icon" viewBox="0 0 12 12"><path d="M0 2h12v8H0z M1 3l5 3.5L11 3" stroke="var(--card)" stroke-width="1"/></svg>
        <span>corvin@corvinhalden.com</span>
      </li>
      <li>
        <svg class="icon" viewBox="0 0 12 12"><circle cx="6" cy="6" r="5.5"/><path d="M0.5 6h11M6 0.5v11M6 0.5c-3 3-3 8 0 11M6 0.5c3 3 3 8 0 11" stroke="var(--card)" stroke-width="0.8" fill="none"/></svg>
        <span>corvinhalden.com</span>
      </li>
      <li>
        <svg class="icon" viewBox="0 0 12 12"><rect x="3" y="0" width="6" height="12" rx="1"/><rect x="4" y="1.5" width="4" height="7" fill="var(--card)"/></svg>
        <span>555.010.2841</span>
      </li>
      <li>
        <svg class="icon" viewBox="0 0 12 12"><path d="M2.5 0.5l2 2.5-1.2 1.5a7 7 0 0 0 4.2 4.2L9 7.5l2.5 2-1.5 2C5 11.5 0.5 7 0.5 2z"/></svg>
        <span>555.010.3916</span>
      </li>
      <li>
        <svg class="icon" viewBox="0 0 12 12"><rect x="0.5" y="4" width="11" height="7.5" rx="1"/><path d="M1 4.5C1 1 11 1 11 4.5" stroke="var(--gold)" stroke-width="1.5" fill="none"/><circle cx="6" cy="7.8" r="1.8" fill="var(--card)"/></svg>
        <span>555.010.4472</span>
      </li>
    </ul>
  </section>

  <section class="card card-front" aria-label="Card front">
    <div class="frame-outer"></div>
    <div class="frame-inner"></div>
    <div class="brand">
      <div class="brand-square"></div>
      <p class="brand-name">Corvin Halden</p>
    </div>
  </section>

</main>
</body>
</html>
```